Visitenkarten-Design für Psychiaterin
Zielgruppe
Dr. med. Monika Haberl, Ärztin, Psychotherapie für Kinder Jugendliche und Erwachsene, spezialisiert auf komplexe Posttraumatische Belastungsstörung, Dissoziative Störungen, Persönlichkeitsstörungen, Bindungsstörungen, LUMO-Mentorin
Das Design soll modern sein, Seriosität Professionalität, Dynamik und Geborgenheit ausstrahlen. Zielgruppe sind Menschen die traumatische Situationen überlebt haben.
Aufgabenstellung
Name, Fachgebiet und Spezialisierung, Telefonnummer, e-Mail
Unter Dateiupload sind Visitenkartenbeispiele die mir gefallen

```html
<!DOCTYPE html>
<html lang="de">
<head>
<meta charset="utf-8">
<title>Visitenkarte – Dr. med. Monika Haberl</title>
<link href="https://fonts.googleapis.com/css2?family=Montserrat:wght@400;500&family=Open+Sans:wght@400&family=Merriweather:wght@400&display=swap" rel="stylesheet">
<style>
  :root {
    --bg: #e4e8ea;
    --card: #ffffff;
    --yellow: #fbe35a;
    --yellow-soft: #fdf3bd;
    --yellow-deep: #f3d321;
    --ink: #2e2e2e;
    --ink-soft: #444444;
  }
  * { margin: 0; padding: 0; box-sizing: border-box; }
  html, body { width: 1200px; height: 900px; overflow: hidden; }
  body {
    background: var(--bg);
    display: flex;
    flex-direction: column;
    align-items: center;
    justify-content: center;
    gap: 50px;
  }
  .card {
    position: relative;
    width: 665px;
    height: 380px;
    background: var(--card);
    overflow: hidden;
    box-shadow: 0 3px 0 #d4d7d9, 0 6px 14px rgba(0,0,0,0.08);
  }
  .wash {
    position: absolute;
    border-radius: 48% 52% 45% 55% / 52% 46% 54% 48%;
    background: radial-gradient(circle at 45% 45%, var(--yellow-soft) 0%, rgba(253,243,189,0.75) 60%, rgba(253,243,189,0) 100%);
  }
  .front .wash { width: 360px; height: 360px; right: -70px; top: -70px; }
  .back .wash { width: 330px; height: 330px; right: -90px; top: -60px; }

  .tab {
    position: absolute;
    left: 62px; top: 0;
    width: 46px; height: 128px;
    background: var(--yellow);
    border-radius: 0 0 23px 23px;
  }
  .tab svg { position: absolute; left: 13px; bottom: 10px; }

  .name-block { position: absolute; left: 140px; top: 60px; }
  .name {
    font-family: "Montserrat", sans-serif;
    font-weight: 500;
    font-size: 30px;
    letter-spacing: 1.5px;
    color: var(--ink);
  }
  .title {
    font-family: "Montserrat", sans-serif;
    font-size: 15px;
    color: var(--ink);
    margin-top: 2px;
  }

  .contact-list { position: absolute; left: 62px; top: 150px; list-style: none; }
  .contact-list li {
    display: flex;
    align-items: flex-start;
    gap: 32px;
    margin-bottom: 14px;
  }
  .icon {
    flex: none;
    width: 30px; height: 30px;
    border-radius: 50%;
    background: var(--yellow);
    display: flex; align-items: center; justify-content: center;
  }
  .contact-text {
    font-family: "Montserrat", sans-serif;
    font-size: 14px;
    color: var(--ink);
    line-height: 30px;
  }
  .focus-text {
    font-family: "Open Sans", sans-serif;
    font-size: 12.5px;
    line-height: 18px;
    color: var(--ink-soft);
    max-width: 430px;
    padding-top: 4px;
  }

  .back-mark {
    position: absolute;
    left: 130px; top: 140px;
    width: 96px; height: 96px;
    border-radius: 50%;
    background: radial-gradient(circle at 45% 40%, #f8e04a 0%, var(--yellow-deep) 70%, #f6dc4a 100%);
  }
  .back-text { position: absolute; left: 168px; top: 156px; }
  .back-name {
    font-family: "Montserrat", sans-serif;
    font-weight: 500;
    font-size: 30px;
    letter-spacing: 1px;
    color: var(--ink);
  }
  .back-sub {
    font-family: "Merriweather", serif;
    font-size: 12.5px;
    color: var(--ink);
    margin-top: 4px;
  }
</style>
</head>
<body>

  <section class="card front">
    <div class="wash" role="img" aria-label="Zarter gelber Aquarellfleck"></div>
    <div class="tab">
      <svg width="20" height="20" viewBox="0 0 20 20" aria-hidden="true">
        <circle cx="10" cy="6" r="4" fill="#fff"/>
        <path d="M2 18c0-4.5 3.6-7 8-7s8 2.5 8 7z" fill="#fff"/>
      </svg>
    </div>
    <div class="name-block">
      <h1 class="name">MONIKA HABERL</h1>
      <p class="title">Dr. med.</p>
    </div>
    <ul class="contact-list">
      <li>
        <span class="icon">
          <svg width="16" height="16" viewBox="0 0 16 16" aria-hidden="true">
            <path d="M2 5c0-2 2.5-3 6-3s6 1 6 3v1h-3V5H5v1H2z" fill="#fff"/>
            <rect x="3" y="7" width="10" height="7" rx="2" fill="#fff"/>
            <circle cx="8" cy="10.5" r="1.8" fill="var(--yellow)"/>
          </svg>
        </span>
        <span class="contact-text">+049 321 5580</span>
      </li>
      <li>
        <span class="icon">
          <svg width="16" height="16" viewBox="0 0 16 16" fill="none" stroke="#fff" stroke-width="1.3" aria-hidden="true">
            <circle cx="8" cy="8" r="6"/>
            <ellipse cx="8" cy="8" rx="2.6" ry="6"/>
            <path d="M2 8h12M3 5h10M3 11h10"/>
          </svg>
        </span>
        <span class="contact-text">www.praxis-haberl.de</span>
      </li>
      <li>
        <span class="icon">
          <svg width="14" height="14" viewBox="0 0 14 14" fill="none" stroke="#fff" stroke-width="1.8" stroke-linecap="round" stroke-linejoin="round" aria-hidden="true">
            <path d="M3 7.5l2.6 2.6L11 4"/>
          </svg>
        </span>
        <p class="focus-text">Psychotherapie für Kinder Jugendliche und Erwachsene, spezialisiert auf komplexe Posttraumatische Belastungsstörung, Dissoziative Störungen, Persönlichkeitsstörungen, Bindungsstörungen, LUMO-Mentorin</p>
      </li>
    </ul>
  </section>

  <section class="card back">
    <div class="wash" role="img" aria-label="Zarter gelber Aquarellfleck"></div>
    <div class="back-mark" role="img" aria-label="Gelber Aquarellkreis"></div>
    <div class="back-text">
      <h2 class="back-name">Dr. med. MONIKA HABERL</h2>
      <p class="back-sub">Psychotherapie für Kinder Jugendliche und Erwachsene</p>
    </div>
  </section>

</body>
</html>
```